Quillon - Energy management company website design

We are interested in a total redesign of our website at www.quillonpowerco.co.uk. We are happy with our current colour scheme and logo but are ready for a new website.

The site is running on a CMS called Umbraco and will remain on this CMS. We are just looking for the html/css and js files so I can build the templates.

We are looking for a home page and maybe a couple of different types of content page. We would like the site to look clean and professional but not necessarily like every other corporate website.
We are really open to any design ideas, we've left the brief quite ambiguous for that reason. We are happy to consider any design no matter how unorthodox as long as it remains professional.

Target Market(s)

Large Businesses

Industry/Entity Type

It Company

Coding

Coded - Design and coding required

Number of Pages Required

3 page

Font styles to use
Sans Serif

Requirements
Must have
• We need a landing page designed and possibly two different kinds of content page allowing for different styles of content. We will want the css and js code with the pages.
• On the home page we would like Two prominent articles/products.
• Then a selection of our other products/services.
• Testimonials, Case studies and News Articles.
• Company colours:
• Text and topleft arrow blue (dark):
• R: 0 G: 96 B: 167
• Red Text and Arrow:
• R: 237 G: 27 B: 35
• Bottom left arrow blue (medium):
• R: 0 G: 174 B: 239
• Bottom right arrow blue (light):
• R: 171 G: 225 B: 250
Nice to have
• We are open to a potentially radical redesign of the site, it doesn't necessarily need to look like every other corporate website.
• We would like to see one or two designs base on this type of imagery:
• http://vuz.lk/PaRmet
• http://vuz.lk/3Hbxno
• http://vuz.lk/K4FUdj

```html
<!DOCTYPE html>
<html lang="en">
<head>
<meta charset="utf-8">
<title>Quillon – Integrated Energy Experts</title>
<link href="https://fonts.googleapis.com/css2?family=Roboto:wght@400;500;700&family=Open+Sans:ital,wght@0,400;0,600;1,400&display=swap" rel="stylesheet">
<style>
:root{
  --blue-dark:#0060a7;
  --blue-nav:#1a5fae;
  --blue-nav-dark:#0d4a92;
  --blue-mid:#00aeef;
  --blue-light:#abe1fa;
  --red:#ed1b23;
  --ink:#2b2b2b;
  --body:#3a3a3a;
  --grey-band:#ebebeb;
  --line:#d6d6d6;
  --footer:#2a2a2a;
}
*{box-sizing:border-box;margin:0;padding:0}
html,body{width:1200px;height:2497px;overflow:hidden;background:#fff}
body{font-family:"Open Sans",sans-serif;color:var(--body);position:relative}
.wrap{width:1000px;margin:0 auto;position:relative}
h2{font-family:"Roboto",sans-serif;font-weight:700;font-size:23px;color:var(--ink);text-align:center;letter-spacing:.2px}

/* header */
.site-header{height:171px;position:relative}
.brand{position:absolute;left:100px;top:38px;display:flex;align-items:center;gap:12px}
.brand-dot{width:60px;height:60px;border-radius:50%;background:var(--blue-dark)}
.brand-name{font-family:"Roboto",sans-serif;font-weight:700;font-size:44px;color:var(--blue-dark);letter-spacing:1px}
.callus{position:absolute;right:100px;top:30px;font-family:"Roboto",sans-serif;font-weight:700;font-size:19px;color:var(--blue-dark)}
.social{position:absolute;right:100px;top:78px;display:flex;gap:12px}
.social span{width:27px;height:27px;display:block;background:var(--blue-dark)}
.main-nav{position:absolute;left:100px;top:145px;width:1000px;height:63px;z-index:2;display:flex;
  background:linear-gradient(var(--blue-nav),var(--blue-nav-dark))}
.main-nav a{flex:1;display:flex;align-items:center;justify-content:center;color:#fff;text-decoration:none;
  font-family:"Roboto",sans-serif;font-size:13px;border-right:1px solid rgba(0,0,0,.18)}
.main-nav a:last-child{border-right:0}

/* hero */
.hero{position:absolute;top:171px;left:0;width:1200px;height:500px;
  background:linear-gradient(180deg,#6fa8d8 0%,#9cc7e6 22%,#3f6b4c 45%,#2f7f83 70%,#1c9aa6 100%)}
.hero-text{position:absolute;top:218px;width:100%;text-align:center;color:#fff;font-family:"Roboto",sans-serif}
.hero-title{font-size:33px;font-weight:500;letter-spacing:.5px}
.hero-sub{font-size:23px;margin-top:22px;letter-spacing:.3px}
.hero-sub em{font-style:normal;color:var(--red)}
.dots{position:absolute;top:459px;left:570px;display:flex;gap:4px}
.dots span{width:11px;height:11px;border-radius:50%;border:2px solid #fff}
.dots span.on{border-color:var(--red)}

/* welcome */
.welcome{position:absolute;top:671px;left:0;width:1200px;height:219px}
.welcome h2{margin-top:55px}
.welcome p{width:1000px;margin:20px auto 0;text-align:center;font-size:13px;line-height:21px}

/* services */
.services{position:absolute;top:890px;left:0;width:1200px;height:521px;background:var(--grey-band)}
.services h2{margin-top:46px}
.service{position:absolute;top:105px;width:278px;text-align:center}
.service .photo{height:196px;border:4px solid #fff;box-shadow:0 0 0 1px var(--line)}
.service h3{font-family:"Roboto",sans-serif;font-weight:700;font-size:15px;color:var(--blue-dark);margin-top:37px}
.service p{font-size:12px;line-height:22px;margin:14px 18px 0}
.more{display:inline-block;font-size:12px;color:var(--blue-dark);margin-top:14px}
.arrow{position:absolute}

/* news */
.news{position:absolute;top:1411px;left:0;width:1200px;height:334px}
.news h2{margin-top:56px}
.post{position:absolute;top:117px;width:300px}
.date{position:absolute;left:0;top:0;width:66px;height:73px;background:var(--blue-dark);color:#fff;text-align:center;
  font-family:"Roboto",sans-serif;font-weight:700;font-size:15px;line-height:22px;padding-top:13px}
.post h4{margin-left:80px;font-family:"Roboto",sans-serif;font-weight:700;font-size:14px;color:var(--ink);padding-top:6px}
.post h5{margin-left:80px;font-family:"Roboto",sans-serif;font-weight:400;font-size:14px;color:var(--ink);margin-top:14px}
.post p{font-size:12px;line-height:22px;margin-top:28px}
.post .more{margin-top:12px}
.divider{position:absolute;top:117px;width:1px;height:155px;background:var(--line)}

/* testimonials */
.testimonials{position:absolute;top:1745px;left:0;width:1200px;height:305px;background:var(--grey-band)}
.testimonials h2{margin-top:50px}
.avatar{position:absolute;left:565px;top:97px;width:70px;height:70px;border-radius:50%;border:3px solid #fff;
  background:linear-gradient(#b88a6a,#7a5544);box-shadow:0 0 0 1px var(--line)}
.quote{position:absolute;top:190px;width:100%;text-align:center;font-style:italic;font-size:13px;line-height:23px;color:var(--ink)}
.author{position:absolute;top:247px;width:100%;text-align:center;font-style:italic;font-size:13px;color:var(--blue-dark)}

/* case studies */
.cases{position:absolute;top:2050px;left:0;width:1200px;height:383px}
.cases h2{margin-top:56px}
.case{position:absolute;left:103px;top:90px;width:997px}
.crest{position:absolute;left:0;top:0;width:70px;height:80px;display:flex;flex-direction:column;align-items:center;gap:4px}
.crest span{width:50px;height:56px;background:var(--blue-dark);display:block}
.crest b{font-family:"Roboto",sans-serif;font-weight:700;font-size:12px;color:var(--blue-dark)}
.case p{margin-left:93px;font-size:13px;line-height:21px;padding-top:14px}
.client{position:absolute;top:206px;width:141px;height:107px;border:2px solid #ececec;display:flex;align-items:center;justify-content:center;
  font-family:"Roboto",sans-serif;font-weight:700;font-size:16px;color:var(--blue-dark);text-align:center;padding:6px}

/* footer */
.site-footer{position:absolute;top:2433px;left:0;width:1200px;height:64px;background:var(--footer);color:#8c8c8c;
  font-size:12px;text-align:center;line-height:64px}
</style>
</head>
<body>

<header class="site-header">
  <div class="brand"><span class="brand-dot"></span><span class="brand-name">Quillon</span></div>
  <div class="callus">CALL US ON: 0800 555 0172</div>
  <div class="social" aria-label="Social links"><span></span><span></span><span></span></div>
</header>

<nav class="main-nav">
  <a href="#">HOME</a><a href="#">OUR SERVICES</a><a href="#">OUR CUSTOMERS</a><a href="#">PULSE</a><a href="#">COMPANY</a><a href="#">BLOG</a><a href="#">CONTACT US</a>
</nav>

<section class="hero" role="img" aria-label="Tropical lagoon with limestone cliffs and a moored outrigger boat">
  <div class="hero-text">
    <div class="hero-title">ENERGY SERVICES : ANALYSIS</div>
    <div class="hero-sub">UNCOVERING THE UNDERLYING <em>COST OF ENERGY</em></div>
  </div>
  <div class="dots"><span class="on"></span><span></span><span></span><span></span></div>
</section>

<section class="welcome">
  <h2>WELCOME TO QUILLON INTEGRATED ENERGY EXPERTS</h2>
  <p>Lorem ipsum dolor sit amet, cum an cibo oratio, dico vidit rebum his ne, ex debitis deterruisset vis. Salutandi laboramus concludaturque vel ex. Augue ocurreret sententiae ei est, at rationibus consetetur per. Ne vis quas nostrud, ea libris everti discere cum. Apeirian reprimique sit et, vel in quot debitis facilis.Lorem ipsum dolor sit amet, cum an cibo oratio, dico vidit rebum his ne, ex debitis deterruisset vis. Salutandi laboramus concludaturque vel ex.</p>
</section>

<section class="services">
  <h2>OUR SERVICES</h2>
  <svg class="arrow" style="left:34px;top:186px" width="20" height="40" viewBox="0 0 20 40"><polyline points="18,2 2,20 18,38" fill="none" stroke="#b5b5b5" stroke-width="2"/></svg>
  <svg class="arrow" style="left:1146px;top:186px" width="20" height="40" viewBox="0 0 20 40"><polyline points="2,2 18,20 2,38" fill="none" stroke="#b5b5b5" stroke-width="2"/></svg>
  <div class="service" style="left:136px">
    <div class="photo" role="img" aria-label="Wind turbines silhouetted against a sunset sky" style="background:linear-gradient(#2f6fb8,#8fb7dd 55%,#f0d9a0 85%,#3a3020)"></div>
    <h3>ENERGY PROCUREMENT</h3>
    <p>We will identify your individual energy procure-ment requirements and work in partnership with you to develop a purchasing</p>
    <a class="more" href="#">[ Read More ]</a>
  </div>
  <div class="service" style="left:461px">
    <div class="photo" role="img" aria-label="Sunset over a rocky shoreline with flowing water" style="background:linear-gradient(#3b4456,#d98a4e 40%,#6f6a6a 65%,#2f3a44)"></div>
    <h3>ENERGY EFFICIENCY</h3>
    <p>We will identify your individual energy procure-ment requirements and work in partnership with you to develop a purchasing</p>
    <a class="more" href="#">[ Read More ]</a>
  </div>
  <div class="service" style="left:785px">
    <div class="photo" role="img" aria-label="Row of light bulbs with one glowing" style="background:linear-gradient(90deg,#1d3f66,#2e5f8f 60%,#e6eef5)"></div>
    <h3>ENERGY ANALYSIS</h3>
    <p>We will identify your individual energy procure-ment requirements and work in partnership with you to develop a purchasing</p>
    <a class="more" href="#">[ Read More ]</a>
  </div>
</section>

<section class="news">
  <h2>LATEST NEWS</h2>
  <article class="post" style="left:100px">
    <div class="date">JAN<br>15</div>
    <h4>ENERGY VIEW MARKET UPDATE</h4><h5>Loreum Ipsum Dolor Sit</h5>
    <p>Qui in everti gubergren, error definitionem an<br>Nec eu munere voluptua eleifend.</p>
    <a class="more" href="#">[ Read More ]</a>
  </article>
  <div class="divider" style="left:419px"></div>
  <article class="post" style="left:454px">
    <div class="date">JAN<br>30</div>
    <h4>ENERGY VIEW MARKET UPDATE</h4><h5>Loreum Ipsum Dolor Sit</h5>
    <p>Qui in everti gubergren, error definitionem an<br>Nec eu munere voluptua eleifend.</p>
    <a class="more" href="#">[ Read More ]</a>
  </article>
  <div class="divider" style="left:775px"></div>
  <article class="post" style="left:807px">
    <div class="date">DEC<br>05</div>
    <h4>ENERGY VIEW MARKET UPDATE</h4><h5>Loreum Ipsum Dolor Sit</h5>
    <p>Qui in everti gubergren, error definitionem an<br>Nec eu munere voluptua eleifend.</p>
    <a class="more" href="#">[ Read More ]</a>
  </article>
</section>

<section class="testimonials">
  <h2>CUSTOMER TESTIMONIALS</h2>
  <svg class="arrow" style="left:428px;top:112px" width="20" height="40" viewBox="0 0 20 40"><polyline points="18,2 2,20 18,38" fill="none" stroke="#b5b5b5" stroke-width="2"/></svg>
  <div class="avatar" role="img" aria-label="Portrait of the customer"></div>
  <svg class="arrow" style="left:768px;top:112px" width="20" height="40" viewBox="0 0 20 40"><polyline points="2,2 18,20 2,38" fill="none" stroke="#b5b5b5" stroke-width="2"/></svg>
  <p class="quote">“In April 2001, we decided to transfer our business to Quillon after using the services of another management company. 11 years later, we have no<br>regrets. We would recommend Quillon to any company that wishes to save money.”</p>
  <p class="author">-Martin Crale</p>
</section>

<section class="cases">
  <h2>CASE STUDIES</h2>
  <div class="case">
    <div class="crest"><span></span><b>Harbourside</b></div>
    <p>Founding members of the Football League, Harbourside FC have competed in the in the top division of English Football for a record 109 seasons. Their 40,000 seater stadium at Millbrook Park and 55 acre training facility at Larkfield Grange are part of Quillon’s Energy Procurement Portfolio.</p>
  </div>
  <div class="client" style="left:103px">Veldor</div>
  <div class="client" style="left:275px">Northgate Airport</div>
  <div class="client" style="left:444px">Alutrex</div>
  <div class="client" style="left:616px">Corvane</div>
  <div class="client" style="left:785px">Brookvale</div>
  <div class="client" style="left:955px">Steinholt</div>
</section>

<footer class="site-footer">Copyright @ 2015 Quillon.All Rights Reserved.</footer>

</body>
</html>
```